Harbor Learning Center Posters Showing Building Blocks

We need poster designs for a School in Arizona for kids with Autism. There will be 4 such posters needed which highlight our schools building blocks. Requirements for all 4 posters are as followed: 1) We need the Harbor Learning Center Logo on each poster. I have included attachment. 2) The posters need the following titles: Building Block #1 (for the first poster), Building Block #2 for the 2nd poster, Building Block #3 for the 3rd poster, and Building Block #4 for the forth poster. 3) The main text and focus of the posters will be the following key words: For the first poster the words "Kids first in every decision". The words for the second poster are: "Students are friends with each other, and welcome new students with open arms." The words for the 3rd poster are: "The school is quiet, and students are working hard to do their best." The words for the 4th poster are: "Parents see amazing improvement in their child." 4) We would love to use some of the kids art from our schools if possible. Use your expertise to decide. I will send these out as well. 5) Try and design the posters around the key words from each poster 6) I am sure if landscape or portrait would be best so I will let the experts decide. All 4 posters need to be the same layout once decided.

Target Market(s)

These posters are for the school only. Prospective students/parents will see these posters so they will be used for Marketing from that perspective. We may put out into local community in future.

Industry/Entity Type

School

Font styles to use
Serif

Requirements
Must have
• 1) Logo (Harbor Learning Center for Growth and Discovery)
• 2) Title: as described in write up
• 3) Key words: as described in write up
Nice to have
• Kids art from school. Note: This is the first time that I have been on this site so I may have made a mistake by putting 4 posters on one project. I am assuming that I would need to pay more to have 4 posters so let me know if I need to modify the project in any way?

```html
<!DOCTYPE html>
<html lang="en">
<head>
<meta charset="utf-8">
<title>Harbor Learning Center – Building Block #4</title>
<link href="https://fonts.googleapis.com/css2?family=Tinos:wght@400&family=Gochi+Hand&display=swap" rel="stylesheet">
<style>
  :root {
    --backdrop: #e4e4e2;
    --paper: #ffffff;
    --ink: #1b1b1b;
    --accent-red: #d0282a;
    --navy: #1f3a8a;
    --leaf: #3f7a4a;
    --aged: #e6d3ad;
    --aged-edge: #c9ad7c;
    --art-orange: #f06a1c;
    --art-navy: #1d2458;
    --art-green: #2e6b4e;
  }
  * { margin: 0; padding: 0; box-sizing: border-box; }
  html, body {
    width: 1200px; height: 1148px; overflow: hidden;
    background: var(--backdrop);
  }
  .poster {
    position: absolute; left: 230px; top: 29px;
    width: 740px; height: 1090px;
    background: var(--paper);
    box-shadow: 0 6px 24px rgba(0,0,0,.12);
  }
  .brand {
    position: absolute; left: 96px; top: 96px;
    display: flex; align-items: flex-start; gap: 14px;
    font-family: "Tinos", "Times New Roman", serif;
    font-weight: 400; color: var(--ink);
  }
  .brand-square {
    width: 40px; height: 40px; margin-top: 4px;
    background: var(--ink);
  }
  .brand-name { font-size: 34px; line-height: 1.15; }
  .brand-tagline { font-size: 25px; line-height: 1.3; }
  .block-title {
    position: absolute; right: 96px; top: 250px;
    font-family: "Tinos", "Times New Roman", serif;
    font-size: 14px; letter-spacing: .02em;
    color: var(--accent-red);
  }
  .artwork-print {
    position: absolute; left: 92px; top: 322px;
    width: 560px; height: 372px;
    padding: 16px;
    background: linear-gradient(135deg, var(--aged), #f1e2c2 50%, var(--aged-edge));
    box-shadow: 4px 8px 14px rgba(0,0,0,.35);
  }
  .artwork-fill {
    width: 100%; height: 100%;
    background:
      linear-gradient(180deg, var(--art-orange) 0%, #e4561a 40%, var(--art-green) 62%, var(--art-navy) 100%);
  }
  .key-words {
    position: absolute; left: 150px; top: 810px;
    font-family: "Gochi Hand", cursive;
    transform: rotate(-13deg);
    transform-origin: left top;
  }
  .key-words span { display: block; white-space: nowrap; }
  .kw-lead { color: var(--navy); font-size: 46px; margin-left: 30px; }
  .kw-focus { color: var(--accent-red); font-size: 74px; line-height: 1; margin-left: 40px; }
  .kw-close { color: var(--leaf); font-size: 40px; margin-left: 220px; }
</style>
</head>
<body>
  <main class="poster">
    <header class="brand">
      <div class="brand-square"></div>
      <div>
        <div class="brand-name">HARBOR LEARNING CENTER</div>
        <div class="brand-tagline">for Growth and Discovery</div>
      </div>
    </header>
    <div class="block-title">SCHOOL BUILDING BLOCK #4</div>

    <figure class="artwork-print">
      <div class="artwork-fill" role="img" aria-label="Student painting in bright orange, navy and green strokes, shown as an aged print"></div>
    </figure>

    <p class="key-words">
      <span class="kw-lead">Parents see amazing</span>
      <span class="kw-focus">improvement</span>
      <span class="kw-close">in their child..</span>
    </p>
  </main>
</body>
</html>
```